Brightholm Cleaning & Maintenance
BCM-Website
Hello Quorvex,
I apologize for any similarities in the banner image, I was less careful in looking at all the draft here, once again I apologize, I was not immediately remove the banner image is the same as you,
thank you.
Hello velstrand
your draft #26 is a derivative of our original draft #19. Please remove it immediately.
Is site admin listening?
We Are A Eco friendly commercial cleaning company not just a lawn service please submit design images featuring our other services outlined in the brief, additionally we have uploaded our current logo design and marketing collateral for design consistancy. Thank you for your interest in this project
BCM
Project has been extended for 3 more days.
Derek
Are you looking for a web design? or are you looking for a html-coded pages?
Designers: Do not upload logo drafts. This is a web project.
I have the logo files and marketing files

```html
<!DOCTYPE html>
<html lang="en">
<head>
<meta charset="utf-8">
<title>BCM - Brightholm Cleaning &amp; Maintenance</title>
<link href="https://fonts.googleapis.com/css2?family=Arimo:wght@400;700&display=swap" rel="stylesheet">
<style>
:root{
  --green:#2f8a1c;
  --green-dark:#1f6a10;
  --green-light:#4aa92b;
  --orange:#f26b1d;
  --ink:#333;
  --muted:#555;
  --page:#ffffff;
  --band:#eef4ea;
  --line:#d6d6d6;
}
*{margin:0;padding:0;box-sizing:border-box}
html,body{width:1200px;height:1004px;overflow:hidden;background:var(--page);font-family:"Arimo",Arial,sans-serif;color:var(--ink)}
.canvas{position:relative;width:1200px;height:1004px;background:linear-gradient(#fff 0,#fff 760px,var(--band) 780px,var(--band) 960px)}
.brand{position:absolute;left:169px;top:30px;display:flex;align-items:center;gap:12px}
.brand-mark{width:26px;height:26px;border-radius:50%;background:var(--green)}
.brand-name{font-size:34px;font-weight:400;color:var(--green-dark)}
.tagline{position:absolute;left:505px;top:26px;padding-left:14px;border-left:2px solid var(--line);font-size:17px;line-height:22px;color:var(--ink)}
.tagline em{font-style:normal;color:var(--green)}
.tagline .amp{color:var(--orange)}
.phone{position:absolute;left:865px;top:22px;display:flex;align-items:center;gap:10px;font-size:24px;color:var(--ink)}
.quote-btn{position:absolute;left:890px;top:54px;width:147px;height:36px;border-radius:6px;background:var(--orange);color:#fff;font-size:15px;display:flex;align-items:center;justify-content:center;gap:8px}
.hero{position:absolute;left:163px;top:109px;width:873px;height:250px;border:1px solid var(--line);display:flex}
.hero-photo{width:620px;height:100%;background:linear-gradient(90deg,#9a9383,#d9d6cc 45%,#cfc9bb 70%,#8c8472)}
.welcome{flex:1;padding:10px 10px;background:#fff}
.welcome h1{font-size:24px;font-weight:400;color:#fff;background:var(--green);padding:2px 8px;margin:-10px -10px 8px}
.welcome p{font-size:12.5px;line-height:16px;color:var(--muted);margin-bottom:8px}
.welcome .more{display:block;text-align:right;font-size:12px;font-weight:700;color:var(--ink)}
.nav{position:absolute;left:163px;top:362px;width:873px;height:36px;background:linear-gradient(var(--green-light),var(--green-dark));display:flex;list-style:none}
.nav li{flex:1;color:#fff;font-size:15px;display:flex;align-items:center;justify-content:center;border-right:1px solid rgba(255,255,255,.35)}
.nav li.active{background:var(--orange);flex:.85}
.tile{position:absolute;width:268px;height:143px;border:1px solid var(--line)}
.tile .shot{position:absolute;inset:0}
.tile h3{position:absolute;right:0;top:6px;background:#fff;font-size:15px;font-weight:400;padding:3px 8px;color:var(--ink)}
.tile .details{position:absolute;right:4px;bottom:4px;background:#111;color:#fff;font-size:10px;font-weight:700;padding:3px 6px}
.t1{left:163px;top:435px}.t2{left:466px;top:435px}.t3{left:767px;top:435px}
.t4{left:163px;top:598px}.t5{left:466px;top:598px}.t6{left:767px;top:598px}
.about{position:absolute;left:174px;top:788px;width:540px}
.about h2,.testimonials h2{font-size:17px;font-weight:400;color:var(--ink);margin-bottom:10px}
.about p{font-size:12px;line-height:15px;color:var(--muted);margin-bottom:12px}
.about .more,.testimonials .who{font-size:12px;color:var(--orange)}
.testimonials{position:absolute;left:776px;top:788px;width:262px}
.testimonials p{font-size:12px;line-height:15px;color:var(--muted);margin-bottom:12px}
.footer{position:absolute;left:0;top:971px;width:1200px;height:33px;background:linear-gradient(var(--green-light),var(--green-dark));color:#fff;font-size:11px;display:flex;align-items:center;justify-content:space-between;padding:0 164px}
</style>
</head>
<body>
<div class="canvas">
  <div class="brand"><span class="brand-mark"></span><span class="brand-name">Brightholm</span></div>
  <div class="tagline">Your One Stop <em>Cleaning</em><br><span class="amp">&amp;</span> <em>Maintenance</em> Source</div>
  <div class="phone">
    <svg width="30" height="24" viewBox="0 0 30 24"><path d="M3 8c0-4 4-6 12-6s12 2 12 6l-5 2-2-3H10L8 10z" fill="var(--orange)"/><rect x="6" y="12" width="18" height="10" rx="2" fill="var(--orange)"/></svg>
    <span>123 123 1234</span>
  </div>
  <div class="quote-btn">
    <svg width="14" height="14" viewBox="0 0 14 14"><circle cx="7" cy="7" r="7" fill="#fff"/><path d="M5 4l4 3-4 3z" fill="var(--orange)"/></svg>
    Get a Quote
  </div>

  <section class="hero">
    <div class="hero-photo" role="img" aria-label="Bright empty office room with polished floor and large windows"></div>
    <div class="welcome">
      <h1>Welcome to BCM</h1>
      <p>Brightholm Cleaning and Maintenance provides the best in commercial cleaning services and ongoing maintenance with a team-driven, ecologically friendly approach. BCM handles both large and small cleaning clients and projects of all sizes, durations, and requirements.</p>
      <p>One of the major advantages of BCM is our wide variety of services. Clients can choose the cleaning that they need when setting up a new job.</p>
      <span class="more">&raquo;Read More</span>
    </div>
  </section>

  <ul class="nav">
    <li class="active">Home</li><li>About Us</li><li>Affiliates</li><li>Franchising</li><li>Our Services</li><li>What We Do</li><li>FAQ</li><li>Contact Us</li>
  </ul>

  <div class="tile t1"><div class="shot" role="img" aria-label="Row of apartment townhouses with lawn" style="background:linear-gradient(#8fb1cf,#b35a45 45%,#6e8a4c)"></div><h3>Apartment Turnover Service</h3><span class="details">View Details</span></div>
  <div class="tile t2"><div class="shot" role="img" aria-label="Open plan office with desks and computers" style="background:linear-gradient(#c9d3d9,#7f8c94 60%,#5b646a)"></div><h3>Office Commercial Cleaning</h3><span class="details">View Details</span></div>
  <div class="tile t3"><div class="shot" role="img" aria-label="House with a foreclosure for sale sign" style="background:linear-gradient(#a8b8c4,#c8c0b0 50%,#b53a2e 70%,#6c8a4c)"></div><h3>Foreclosure Cleaning</h3><span class="details">View Details</span></div>
  <div class="tile t4"><div class="shot" role="img" aria-label="Checkered tiled floor" style="background:linear-gradient(135deg,#9a9a9a,#e4e4e4 50%,#7a7a7a)"></div><h3>Floor Care</h3><span class="details">View Details</span></div>
  <div class="tile t5"><div class="shot" role="img" aria-label="Green lawn and garden grounds" style="background:linear-gradient(#9fc0d8,#5f8f3a 50%,#3f6b22)"></div><h3>Ground Maintenance</h3><span class="details">View Details</span></div>
  <div class="tile t6"><div class="shot" role="img" aria-label="Blue recycling bins" style="background:linear-gradient(#f2f4f6,#d9e2ea 50%,#2b6fb3)"></div><h3>Recycling Services</h3><span class="details">View Details</span></div>

  <section class="about">
    <h2>About Company</h2>
    <p>An overview of BCM and our commercial cleaning services. Includes information about Brightholm Cleaning and Maintenance and our defining features: Office cleaning, commercial cleaning, apartment cleaning, apartment turnover, foreclosure cleaning, green cleaning, commercial floor care.</p>
    <p>Brightholm Cleaning and Maintenance provides the best in commercial cleaning services and ongoing maintenance with a team-driven, ecologically friendly approach. BCM handles both large and small cleaning clients and projects of all sizes, durations, and requirements.</p>
    <span class="more">&raquo; Read More</span>
  </section>

  <section class="testimonials">
    <h2>Testimonials:</h2>
    <p>&ldquo; Lorem Ipsum is simply dummy text of the printing and typesetting industry. Lorem Ipsum has been the industry's standard dummy text ever since the 1500s.</p>
    <p>When an unknown printer took a galley of type and scrambled it to make a type book.&rdquo;</p>
    <span class="who">&raquo; Happy Customer</span>
  </section>

  <footer class="footer">
    <span>Copyright 2011 B.C.M all rights reserved</span>
    <span>Home | About Us | Our Services | FAQ | Contact Us</span>
  </footer>
</div>
</body>
</html>
```